Business Card Design

We need a business card design for a Non-Profit Christian Based Organization located in Milford, Pa.
Alder Ridge Helping Harbor
Is a Christ-centered organization dedicated to providing compassion and hope to homeless or near homeless, families and individuals, by meeting their basic and urgent need of food, clothing and shelter.
Updates
the logo is black and white
and must add the color green some where 00400
Industry/Entity Type
Clothing
Contact Information for Business Card
Alder Ridge Helping Harbor
P.O. Box 287
Fernbrook, Pa 18402
Phone: (570) 413-CARE(2273)
Toll Free: (855) 413-CARE
email:Info@alderridgehh.org
email:Careline@alderridgehh.org
Our organization already has a logo.
Front of card:
Is a Christ-centered organization dedicated to providing compassion and hope to homeless or near homes, families and individual by meeting their basic and urgent need of food, clothing and shelter.(this is our Mission Statement)
On back of card:
'I was hungry and you gave me something to eat;
"I was thirsty and you gave me something to drink;
"I was a stranger and you invited me in."
Matthew 25:35
Color: Logo is black and white
Background color I would like a bright light green 00ff00(close to that)
I attached a sample of what I created on Quill Press but, I don't like the color green, nor the design (but I just wanted to give you and Idea of the Logo and Alder Ridge (one line) Helping Harbor (second line) in a different font thank you
Delia Rostova
Pr/Board of Directors

```html
<!DOCTYPE html>
<html lang="en">
<head>
<meta charset="utf-8">
<title>Alder Ridge Helping Harbor – Business Card</title>
<link rel="stylesheet" href="https://fonts.googleapis.com/css2?family=Gelasio&family=Tinos&family=Pinyon+Script&display=swap">
<style>
  :root {
    --page-bg: #e4e2df;
    --card-green: #52b94d;
    --strip-white: #ffffff;
    --back-grey: #ececec;
    --ink: #111111;
    --light-ink: #ffffff;
  }
  * { margin: 0; padding: 0; box-sizing: border-box; }
  html, body {
    width: 1200px; height: 1000px; overflow: hidden;
    background: var(--page-bg);
  }
  .canvas { position: relative; width: 1200px; height: 1000px; }

  .card { position: absolute; box-shadow: 0 4px 14px rgba(0,0,0,0.25); }

  /* Front */
  .card-front {
    left: 40px; top: 41px; width: 752px; height: 440px;
    background: var(--card-green);
  }
  .logo-strip {
    position: absolute; left: 48px; top: 0; width: 147px; height: 100%;
    background: var(--strip-white);
    display: flex; align-items: center; justify-content: center;
  }
  .logo-name {
    font-family: "Gelasio", Georgia, serif;
    font-size: 17px; line-height: 1.3; color: var(--ink);
    text-align: center;
  }
  .front-copy {
    position: absolute; left: 195px; right: 30px; top: 0;
    text-align: center; color: var(--light-ink);
  }
  .org-name-primary {
    margin-top: 58px;
    font-family: "Gelasio", Georgia, serif;
    font-size: 52px; font-weight: 400; line-height: 1.1;
  }
  .org-name-script {
    font-family: "Pinyon Script", cursive;
    font-size: 58px; line-height: 1.1; margin-top: 2px;
  }
  .mission {
    margin: 22px auto 0; width: 470px;
    font-family: "Tinos", "Times New Roman", serif;
    font-size: 15.5px; line-height: 33px;
  }

  /* Back */
  .card-back {
    left: 391px; top: 519px; width: 759px; height: 444px;
    background: var(--back-grey); color: var(--ink);
    font-family: "Gelasio", Georgia, serif;
  }
  .back-logo-name {
    position: absolute; left: 12px; bottom: 14px;
    font-size: 15px; line-height: 1.3;
  }
  .scripture {
    position: absolute; left: 0; right: 0; top: 36px;
    text-align: center; font-size: 20px; line-height: 32px;
  }
  .contact {
    position: absolute; left: 0; right: 0; top: 172px;
    text-align: center; font-size: 25.5px; line-height: 33.5px;
    font-style: normal;
  }
</style>
</head>
<body>
<main class="canvas">
  <section class="card card-front" aria-label="Card front">
    <div class="logo-strip">
      <p class="logo-name">Alder Ridge<br>Helping<br>Harbor</p>
    </div>
    <div class="front-copy">
      <h1 class="org-name-primary">Alder Ridge</h1>
      <p class="org-name-script">Helping Harbor</p>
      <p class="mission">Alder Ridge Helping Harbor is a Christ-centered organization dedicated to providing compassion and hope to homeless or near homes, families and individual by meeting their basic and urgent need of food, clothing and shelter.</p>
    </div>
  </section>

  <section class="card card-back" aria-label="Card back">
    <p class="back-logo-name">Alder Ridge<br>Helping Harbor</p>
    <blockquote class="scripture">
      'I was hungry and you gave me something to eat; "I was thirsty and you<br>
      gave me something to drink; "I was a stranger and you invited me in."<br>
      Matthew 25:35
    </blockquote>
    <address class="contact">
      Alder Ridge Helping Harbor<br>
      P.O. Box 287 Fernbrook, Pa 18402<br>
      Phone: (570) 413-CARE(2273)<br>
      Toll Free: (855) 413-CARE<br>
      email:Info@alderridgehh.org<br>
      email:Careline@alderridgehh.org
    </address>
  </section>
</main>
</body>
</html>
```